Fast Reliable Internet Service needs Design Template for marketing brochures

We would like a design template for different types of brochures that would introduce different products that our Internet Service offers. We are fairly new to the area we serve and our new products come available for different areas frequently. I am uploading our company logo, ZELVONET. We may need more than one design based on the product we are trying to introduce to different areas. We need a design that would go on a 11x17 bifold, 6 1/2 x 11 each block parcel brochure, postcards and single page inserts. Some areas we service can receive fiber internet, some fiber and wireless internet, some just wireless. We also offer hosted wi-fi and hosted PBX Phones.

Marketing

```html
<!DOCTYPE html>
<html lang="en">
<head>
<meta charset="utf-8">
<title>ZELVONET — Internet Service Offers Brochure</title>
<link rel="stylesheet" href="https://fonts.googleapis.com/css2?family=Montserrat:ital,wght@0,300;0,500;0,700;0,800;1,800&family=Merriweather:wght@400;700&display=swap">
<style>
  :root {
    --page: #e4e4e6;
    --ink-black: #0d0d0f;
    --ink-dark: #17171a;
    --brand-blue: #2a5cf0;
    --photo-light: #5fd2ff;
    --photo-mid: #1f8fe6;
    --photo-deep: #0b3a8c;
    --paper: #ffffff;
    --row-grey: #d3d3d6;
    --row-light: #e9e9eb;
    --tab-grey: #5a5a5e;
    --text-light: #e8e8ec;
    --text-muted: #9a9aa0;
    --text-dark: #2a2a2e;
    --tick-ink: #2a2a2e;
  }
  * { box-sizing: border-box; margin: 0; padding: 0; }
  html, body { width: 1200px; height: 835px; overflow: hidden; }
  body { background: var(--page); position: relative; font-family: "Montserrat", Arial, sans-serif; }

  /* ---------- Front cover ---------- */
  .cover {
    position: absolute; left: 50px; top: 60px; width: 340px; height: 715px;
    background: var(--ink-black); overflow: hidden;
    box-shadow: 0 6px 18px rgba(0,0,0,.18);
  }
  .cover-photo {
    height: 250px;
    background: linear-gradient(160deg, var(--photo-light) 0%, var(--photo-mid) 45%, var(--photo-deep) 100%);
  }
  .cover-title { position: absolute; left: 0; right: 0; top: 305px; text-align: center; }
  .cover-title .line { display: block; color: var(--paper); font-weight: 500; font-size: 42px; letter-spacing: 1px; line-height: 1.05; text-transform: uppercase; }
  .cover-title .line--accent { color: var(--brand-blue); font-weight: 800; font-style: italic; font-size: 50px; }
  .cover-bar { position: absolute; background: var(--brand-blue); }
  .cover-bar--left { left: 22px; top: 345px; width: 16px; height: 56px; }
  .cover-bar--right { right: 0; top: 360px; width: 34px; height: 100px; }
  .cover-tagline {
    position: absolute; left: 24px; top: 478px; color: var(--paper);
    font-weight: 700; font-size: 13px; letter-spacing: 2px; text-transform: uppercase;
  }
  .cover-tagline .dot { color: var(--brand-blue); padding: 0 4px; }
  .cover-stripe { position: absolute; right: 34px; top: 500px; width: 60px; height: 215px; background: #1e1e22; }
  .cover-brand {
    position: absolute; left: 14px; top: 520px; width: 205px; height: 56px;
    background: var(--paper); border-radius: 10px;
    display: flex; align-items: center; gap: 8px; padding-left: 14px;
  }
  .cover-brand .mark { flex: 0 0 20px; width: 20px; height: 20px; border-radius: 50%; background: var(--brand-blue); }
  .cover-brand .name { color: var(--brand-blue); font-weight: 800; font-size: 22px; letter-spacing: .5px; }

  /* ---------- Inside spread ---------- */
  .spread {
    position: absolute; left: 430px; top: 60px; width: 720px; height: 715px;
    background: var(--paper); overflow: hidden;
    box-shadow: 0 6px 18px rgba(0,0,0,.18);
  }
  .spread-dark { position: absolute; left: 0; top: 0; width: 720px; height: 410px; background: var(--ink-dark); }
  .fold { position: absolute; left: 360px; top: 0; width: 1px; height: 715px; background: rgba(0,0,0,.15); }

  .section-heading { position: absolute; font-weight: 300; font-size: 34px; letter-spacing: .5px; text-transform: lowercase; }
  .section-heading::before {
    content: ""; position: absolute; left: -30px; top: 2px; width: 14px; height: 40px; background: var(--brand-blue);
  }
  .services-heading { left: 30px; top: 22px; color: var(--paper); }
  .services-heading .accent { color: var(--brand-blue); }
  .plans-heading { left: 30px; top: 420px; color: var(--text-dark); }

  .body-copy { position: absolute; font-family: "Merriweather", Georgia, serif; font-size: 10px; line-height: 1.45; }
  .body-copy--light { color: var(--text-light); }
  .body-copy--dark { color: var(--text-muted); }

  .service { position: absolute; display: flex; gap: 12px; width: 320px; }
  .service-box { flex: 0 0 58px; height: 44px; background: var(--paper); border: 3px solid var(--brand-blue); }
  .service-title { font-family: "Merriweather", Georgia, serif; font-weight: 700; font-size: 12px; color: var(--paper); margin-bottom: 3px; }
  .service-text { font-family: "Merriweather", Georgia, serif; font-size: 9.5px; line-height: 1.4; color: var(--text-light); }

  /* ---------- Price table ---------- */
  .feature-list { position: absolute; left: 20px; top: 533px; width: 130px; list-style: none; }
  .feature-list li { height: 20px; line-height: 20px; font-size: 10px; color: var(--text-muted); padding-left: 6px; }
  .feature-list li:nth-child(odd) { background: var(--row-light); }

  .plan { position: absolute; top: 505px; width: 160px; }
  .plan-name {
    height: 24px; line-height: 24px; text-align: center; background: var(--tab-grey);
    color: var(--paper); font-size: 12px; font-weight: 500; border-bottom: 4px solid var(--brand-blue);
    border-radius: 6px 6px 0 0;
  }
  .plan-rows { list-style: none; }
  .plan-rows li { height: 20px; display: flex; align-items: center; justify-content: center; background: var(--row-grey); }
  .plan-rows li:nth-child(even) { background: var(--row-light); }
  .plan-price { margin-top: 7px; height: 26px; line-height: 26px; text-align: center; color: var(--paper); font-weight: 800; font-size: 18px; }
  .plan--starter .plan-price { background: var(--tab-grey); }
  .plan--professional .plan-price { background: var(--brand-blue); }
  .plan--business .plan-price { background: var(--ink-black); }
  .plan-note { margin-top: 4px; font-size: 8px; color: var(--text-muted); text-align: center; }
  .plan--starter { left: 170px; }
  .plan--professional { left: 380px; }
  .plan--business { left: 545px; }
  .tick { width: 13px; height: 13px; }
  .tick circle { fill: var(--paper); stroke: var(--tick-ink); stroke-width: 1.2; }
  .tick path { fill: none; stroke: var(--tick-ink); stroke-width: 1.5; }
</style>
</head>
<body>

<section class="cover" aria-label="Brochure front cover">
  <div class="cover-photo" role="img" aria-label="Close-up photograph of a web address in a glowing blue browser bar"></div>
  <div class="cover-bar cover-bar--left"></div>
  <div class="cover-bar cover-bar--right"></div>
  <h1 class="cover-title">
    <span class="line">Internet</span>
    <span class="line line--accent">Service</span>
    <span class="line">Offers</span>
  </h1>
  <p class="cover-tagline">Design<span class="dot">.</span>Development<span class="dot">.</span>Host</p>
  <div class="cover-stripe"></div>
  <div class="cover-brand"><span class="mark"></span><span class="name">ZELVONET</span></div>
</section>

<section class="spread" aria-label="Brochure inside spread">
  <div class="spread-dark"></div>
  <div class="fold"></div>

  <h2 class="section-heading services-heading">our <span class="accent">services</span></h2>
  <p class="body-copy body-copy--light" style="left:30px;top:74px;width:310px;">Fast, reliable connections for homes and businesses across every area we serve today.</p>

  <div class="service" style="left:30px;top:130px;"><div class="service-box"></div><div><h3 class="service-title">Fiber Internet</h3><p class="service-text">Symmetrical speeds over glass, built for streaming, gaming and busy home offices.</p></div></div>
  <div class="service" style="left:30px;top:215px;"><div class="service-box"></div><div><h3 class="service-title">Fixed Wireless</h3><p class="service-text">Reliable coverage where cable cannot reach, installed by our local team fast.</p></div></div>
  <div class="service" style="left:30px;top:300px;"><div class="service-box"></div><div><h3 class="service-title">Hosted Wi-Fi</h3><p class="service-text">Managed guest and staff networks for shops, cafes, hotels and apartment blocks.</p></div></div>

  <p class="body-copy body-copy--light" style="left:385px;top:40px;width:310px;">Every plan includes local support, free setup and a friendly team nearby.</p>
  <div class="service" style="left:385px;top:110px;"><div class="service-box"></div><div><h3 class="service-title">Hosted PBX</h3><p class="service-text">Cloud phone systems with voicemail, call routing and desk phones you keep.</p></div></div>
  <div class="service" style="left:385px;top:195px;"><div class="service-box"></div><div><h3 class="service-title">Web Hosting</h3><p class="service-text">Fast secure servers for your website, email and files with daily backups.</p></div></div>
  <div class="service" style="left:385px;top:280px;"><div class="service-box"></div><div><h3 class="service-title">Site Design</h3><p class="service-text">Clean modern websites that load quickly and look sharp on every screen.</p></div></div>

  <h2 class="section-heading plans-heading">plans we offer</h2>
  <p class="body-copy body-copy--dark" style="left:385px;top:430px;width:310px;">Pick the plan that fits your home or business and upgrade anytime.</p>

  <ul class="feature-list">
    <li>Speed</li><li>Data</li><li>Wi-Fi router</li><li>Phone line</li><li>Support</li><li>Install</li>
  </ul>

  <div class="plan plan--starter">
    <div class="plan-name">Stater</div>
    <ul class="plan-rows">
      <li><svg class="tick" viewBox="0 0 14 14"><circle cx="7" cy="7" r="6"/><path d="M4 7.2l2 2 4-4.2"/></svg></li>
      <li><svg class="tick" viewBox="0 0 14 14"><circle cx="7" cy="7" r="6"/><path d="M4 7.2l2 2 4-4.2"/></svg></li>
      <li><svg class="tick" viewBox="0 0 14 14"><circle cx="7" cy="7" r="6"/><path d="M4 7.2l2 2 4-4.2"/></svg></li>
      <li><svg class="tick" viewBox="0 0 14 14"><circle cx="7" cy="7" r="6"/><path d="M4 7.2l2 2 4-4.2"/></svg></li>
      <li></li><li></li>
    </ul>
    <div class="plan-price">$56.00</div>
    <p class="plan-note">per month, taxes extra</p>
  </div>

  <div class="plan plan--professional">
    <div class="plan-name">Professional</div>
    <ul class="plan-rows">
      <li><svg class="tick" viewBox="0 0 14 14"><circle cx="7" cy="7" r="6"/><path d="M4 7.2l2 2 4-4.2"/></svg></li>
      <li><svg class="tick" viewBox="0 0 14 14"><circle cx="7" cy="7" r="6"/><path d="M4 7.2l2 2 4-4.2"/></svg></li>
      <li><svg class="tick" viewBox="0 0 14 14"><circle cx="7" cy="7" r="6"/><path d="M4 7.2l2 2 4-4.2"/></svg></li>
      <li><svg class="tick" viewBox="0 0 14 14"><circle cx="7" cy="7" r="6"/><path d="M4 7.2l2 2 4-4.2"/></svg></li>
      <li><svg class="tick" viewBox="0 0 14 14"><circle cx="7" cy="7" r="6"/><path d="M4 7.2l2 2 4-4.2"/></svg></li>
      <li></li>
    </ul>
    <div class="plan-price">$75.00</div>
    <p class="plan-note">per month, taxes extra</p>
  </div>

  <div class="plan plan--business">
    <div class="plan-name">Business</div>
    <ul class="plan-rows">
      <li><svg class="tick" viewBox="0 0 14 14"><circle cx="7" cy="7" r="6"/><path d="M4 7.2l2 2 4-4.2"/></svg></li>
      <li><svg class="tick" viewBox="0 0 14 14"><circle cx="7" cy="7" r="6"/><path d="M4 7.2l2 2 4-4.2"/></svg></li>
      <li><svg class="tick" viewBox="0 0 14 14"><circle cx="7" cy="7" r="6"/><path d="M4 7.2l2 2 4-4.2"/></svg></li>
      <li><svg class="tick" viewBox="0 0 14 14"><circle cx="7" cy="7" r="6"/><path d="M4 7.2l2 2 4-4.2"/></svg></li>
      <li><svg class="tick" viewBox="0 0 14 14"><circle cx="7" cy="7" r="6"/><path d="M4 7.2l2 2 4-4.2"/></svg></li>
      <li><svg class="tick" viewBox="0 0 14 14"><circle cx="7" cy="7" r="6"/><path d="M4 7.2l2 2 4-4.2"/></svg></li>
    </ul>
    <div class="plan-price">$100.00</div>
    <p class="plan-note">per month, taxes extra</p>
  </div>
</section>

</body>
</html>
```